Marriage Celebrant Card Design

My business is called Golden Vows and Keepsakes. I have attached a preview of a card design that I was unable to adapt to card as I am very technically challenged. I like the colors in the card currently purples. Like butterflies for new beginnings. I don't mind a little different.

Industry/Entity Type

Business

Requirements
Must have
• On back would like appointment time and date options

```html
<!DOCTYPE html>
<html lang="en">
<head>
<meta charset="utf-8">
<title>Golden Vows and Keepsakes – Business Card</title>
<link rel="stylesheet" href="https://fonts.googleapis.com/css2?family=Great+Vibes&family=Playball&family=Tinos:ital@0;1&family=Arimo&display=swap">
<style>
  :root {
    --page-bg: #efecf4;
    --card-bg: #ffffff;
    --ink: #111111;
    --violet: #9d6fd0;
    --violet-deep: #5a2a9a;
    --lilac: #a97fd6;
    --lavender: #e6d6f4;
    --lavender-soft: #f4ecfb;
    --photo-grey: #8a8a8a;
    --photo-dark: #3a3a3a;
    --shadow-purple: #6b3ea8;
  }
  * { margin: 0; padding: 0; box-sizing: border-box; }
  html, body { width: 1200px; height: 600px; overflow: hidden; }
  body { background: var(--page-bg); position: relative; font-family: "Tinos", serif; }

  .card { position: absolute; background: var(--card-bg); overflow: hidden; }
  .card--front { left: 61px; top: 77px; width: 650px; height: 401px; }
  .card--back { left: 754px; top: 164px; width: 377px; height: 226px; }

  .art { position: absolute; display: block; }

  /* Front */
  .front-name {
    position: absolute; left: 50px; top: 8px;
    font-family: "Great Vibes", cursive; font-size: 78px; line-height: 1;
    color: var(--ink); white-space: nowrap;
  }
  .front-tagline {
    position: absolute; left: 375px; top: 120px;
    font-family: "Tinos", serif; font-size: 19px; color: var(--lilac); white-space: nowrap;
  }
  .motto-band {
    position: absolute; left: 300px; top: 143px; width: 340px; height: 80px;
    background: linear-gradient(90deg, rgba(230,214,244,0) 0%, var(--lavender) 22%, var(--lavender) 100%);
  }
  .motto {
    position: absolute; left: 325px; top: 150px; width: 320px;
    font-family: "Playball", cursive; font-size: 22px; line-height: 33px;
    color: #ffffff; text-shadow: 1px 1px 1px var(--shadow-purple), 0 0 2px var(--shadow-purple);
    white-space: nowrap;
  }
  .services {
    position: absolute; left: 320px; top: 232px; width: 300px; text-align: center;
    font-family: "Tinos", serif; font-size: 20px; line-height: 22px; color: var(--ink);
  }
  .contact-front { position: absolute; left: 330px; top: 300px; width: 290px; text-align: center; }
  .region {
    font-family: "Playball", cursive; font-size: 30px; line-height: 32px;
    color: var(--lilac); text-shadow: 1px 1px 1px var(--violet-deep);
  }
  .phone { font-family: "Arimo", sans-serif; color: var(--lilac); }
  .email { font-family: "Arimo", sans-serif; color: var(--lilac); }
  .contact-front .phone { font-size: 26px; line-height: 26px; }
  .contact-front .email { font-size: 16px; line-height: 22px; }

  /* Back */
  .back-band {
    position: absolute; left: 0; top: 22px; width: 100%; height: 36px;
    background: linear-gradient(90deg, rgba(230,214,244,0) 0%, var(--lavender) 30%, var(--lavender) 70%, rgba(230,214,244,0) 100%);
  }
  .back-name {
    position: absolute; left: 0; top: 24px; width: 100%; text-align: center;
    font-family: "Great Vibes", cursive; font-size: 38px; line-height: 1; color: var(--ink);
  }
  .appointment { position: absolute; left: 36px; top: 106px; font-size: 10px; color: var(--ink); }
  .appointment__title { display: block; margin-bottom: 6px; }
  .appointment__row { display: flex; align-items: flex-end; height: 18px; }
  .appointment__label { width: 72px; text-align: right; padding-right: 6px; }
  .appointment__line { width: 200px; border-bottom: 1px solid #555; height: 10px; }
  .contact-back { position: absolute; left: 0; top: 172px; width: 100%; text-align: center; }
  .contact-back .region { font-size: 18px; line-height: 18px; text-shadow: none; color: var(--lilac); }
  .contact-back .phone { font-size: 14px; line-height: 14px; }
  .contact-back .email { font-size: 10px; line-height: 13px; }
</style>
</head>
<body>

<section class="card card--front" aria-label="Card front">
  <svg class="art" width="650" height="401" viewBox="0 0 650 401">
    <defs>
      <linearGradient id="wing" x1="0" y1="0" x2="1" y2="1">
        <stop offset="0" stop-color="#c9a8ee"/>
        <stop offset="1" stop-color="#5a2a9a"/>
      </linearGradient>
      <linearGradient id="portrait" x1="0" y1="0" x2="0" y2="1">
        <stop offset="0" stop-color="#9a9a9a"/>
        <stop offset="1" stop-color="#2e2e2e"/>
      </linearGradient>
    </defs>
    <rect role="img" aria-label="Black and white portrait photo of the celebrant seated beside a wooden barrel" x="14" y="92" width="295" height="290" rx="6" fill="url(#portrait)"/>
    <rect role="img" aria-label="Purple butterfly illustration" x="22" y="22" width="82" height="62" rx="20" fill="url(#wing)"/>
    <rect role="img" aria-label="Purple butterfly illustration" x="358" y="22" width="70" height="56" rx="18" fill="url(#wing)"/>
    <rect role="img" aria-label="Purple butterfly illustration" x="428" y="44" width="50" height="40" rx="14" fill="url(#wing)"/>
    <rect role="img" aria-label="Purple butterfly illustration" x="385" y="80" width="44" height="34" rx="12" fill="url(#wing)"/>
    <rect role="img" aria-label="Purple butterfly illustration" x="88" y="88" width="44" height="36" rx="12" fill="url(#wing)"/>
    <rect role="img" aria-label="Purple butterfly illustration" x="36" y="108" width="40" height="34" rx="12" fill="url(#wing)"/>
    <rect role="img" aria-label="Purple butterfly illustration" x="10" y="130" width="62" height="48" rx="16" fill="url(#wing)"/>
    <rect role="img" aria-label="Cluster of purple butterflies" x="64" y="215" width="48" height="110" rx="16" fill="url(#wing)"/>
  </svg>

  <h1 class="front-name">Jo Bellamy</h1>
  <p class="front-tagline">Golden Vows and Keepsakes</p>
  <div class="motto-band"></div>
  <p class="motto">A Journey of Special Moments<br>A Lifetime of Precious Memories</p>
  <p class="services">Weddings | Commitments<br>Namings | Funerals<br>Any Special Occasion</p>
  <div class="contact-front">
    <p class="region">Mid North Coast</p>
    <p class="phone">0400 555 271</p>
    <p class="email">celebbellamy@example.com.au</p>
  </div>
</section>

<section class="card card--back" aria-label="Card back">
  <div class="back-band"></div>
  <svg class="art" width="377" height="226" viewBox="0 0 377 226">
    <defs>
      <linearGradient id="wing-back" x1="0" y1="0" x2="1" y2="1">
        <stop offset="0" stop-color="#c9a8ee"/>
        <stop offset="1" stop-color="#5a2a9a"/>
      </linearGradient>
    </defs>
    <rect role="img" aria-label="Faint butterfly watermark" x="110" y="70" width="150" height="110" rx="36" fill="#e7def0" opacity="0.7"/>
    <rect role="img" aria-label="Faint butterfly watermark" x="270" y="112" width="46" height="46" rx="14" fill="#e7def0" opacity="0.6"/>
    <rect role="img" aria-label="Purple butterfly illustration" x="14" y="16" width="44" height="38" rx="12" fill="url(#wing-back)"/>
    <rect role="img" aria-label="Purple butterfly illustration" x="314" y="20" width="46" height="36" rx="12" fill="url(#wing-back)"/>
  </svg>
  <h2 class="back-name">Jo Bellamy</h2>
  <div class="appointment">
    <span class="appointment__title">Your Appointment</span>
    <div class="appointment__row"><span class="appointment__label">Time :</span><span class="appointment__line"></span></div>
    <div class="appointment__row"><span class="appointment__label">Date :</span><span class="appointment__line"></span></div>
  </div>
  <div class="contact-back">
    <p class="region">Mid North Coast</p>
    <p class="phone">0400 555 271</p>
    <p class="email">celebbellamy@example.com.au</p>
  </div>
</section>

</body>
</html>
```